Export company based in South America (Ecuador) we export flowers, chocolate, and bananas

We need a website that gives our potential clients and introduction into our company and the different types of commodities we export around the world. We are based in Quito, Ecuador so the website should portray the feel of Ecuadorian landscapes within a modern looking website.
At the moment we are exporting roses, chocolate, and bananas so the website should have an intro to our company and then three different areas that describe our three main commodity. The three different sections should explain why each of the products from Ecuador are some of the best in the world in their categories and the benefits of importing the commodity through our company.
Industry/Entity Type
Commodity
Number of Pages Required
4 page

```html
<!DOCTYPE html>
<html lang="en">
<head>
<meta charset="utf-8">
<title>Andevia – Ecuadorian Commodity Exports</title>
<link rel="stylesheet" href="https://fonts.googleapis.com/css2?family=Raleway:wght@400;500;600&family=Poppins:wght@400;500;600;700&family=Lato:wght@400;700&display=swap">
<style>
:root{
  --blue:#1a7fd4;
  --blue-deep:#1369b8;
  --yellow:#f5c000;
  --ink:#222;
  --text:#3a3a3a;
  --cream:#fcefe0;
  --footer:#1d1916;
  --white:#fff;
}
*{box-sizing:border-box;margin:0;padding:0}
html,body{width:1200px;height:4062px;overflow:hidden;background:var(--white)}
body{font-family:"Lato",sans-serif;color:var(--text);position:relative}
.page{position:relative;width:1200px;height:4062px;overflow:hidden}
.abs{position:absolute}
svg{display:block}

/* top bar */
.topbar{left:0;top:0;width:1200px;height:64px;background:var(--blue);color:var(--white);font-family:"Poppins",sans-serif}
.topbar .hours{left:98px;top:10px;display:flex;align-items:center;gap:18px;font-size:15px}
.topbar .phone{left:878px;top:10px;display:flex;align-items:center;gap:14px;font-size:19px;font-weight:600}
.badge{width:44px;height:44px;border-radius:50%;background:var(--white);display:flex;align-items:center;justify-content:center}

/* nav */
.brand{left:95px;top:96px;display:flex;align-items:center;gap:14px;font-family:"Poppins",sans-serif;font-weight:700;font-size:24px;letter-spacing:2px;color:var(--ink)}
.brand .dot{width:50px;height:50px;border-radius:50%;background:var(--blue)}
.nav{font-family:"Poppins",sans-serif;font-size:17px;letter-spacing:1px;color:#333}
.nav a{color:inherit;text-decoration:none;position:absolute;white-space:nowrap}

/* hero */
.hero{left:0;top:181px;width:1200px;height:632px}
.hero-title{left:0;top:360px;width:1200px;text-align:center;font-family:"Poppins",sans-serif;font-weight:700;font-size:72px;letter-spacing:6px;color:var(--white);text-shadow:0 3px 8px rgba(0,0,0,.5)}
.hero-sub{left:0;top:468px;width:1200px;text-align:center;font-family:"Raleway",sans-serif;font-size:22px;line-height:41px;color:var(--white);text-shadow:0 1px 4px rgba(0,0,0,.6)}
.btn{display:flex;align-items:center;justify-content:center;background:var(--yellow);color:#222;border-radius:24px;font-family:"Raleway",sans-serif;font-weight:500;font-size:19px}

h2.sec{font-family:"Raleway",sans-serif;font-weight:500;font-size:38px;color:var(--ink);letter-spacing:.5px}
h2.sec span{color:var(--yellow)}
.body-copy{font-size:17px;line-height:36px;color:var(--text)}

/* commodities */
.commodity{width:300px;text-align:center}
.commodity h3{font-family:"Raleway",sans-serif;font-weight:500;font-size:24px;color:var(--ink);margin-bottom:10px}
.commodity p{font-family:"Raleway",sans-serif;font-size:18px;line-height:31px;color:#333}

/* benefits */
.benefit{left:106px;display:flex;align-items:center;gap:18px;font-size:17px;line-height:30px;width:430px}
.benefit .ico{width:60px;height:60px;border-radius:50%;background:var(--yellow);box-shadow:-3px 4px 0 var(--blue);flex:none;display:flex;align-items:center;justify-content:center}

/* why */
.why-copy{color:var(--white);font-family:"Raleway",sans-serif;font-size:18px;line-height:36px}
.ring{width:70px;height:70px;border-radius:50%;background:var(--blue);border:4px solid var(--white);display:flex;align-items:center;justify-content:center}

/* newsletter */
.news-title{font-family:"Raleway",sans-serif;font-size:28px;color:var(--ink);letter-spacing:.5px}
.news-title span{color:var(--yellow);font-weight:600}

/* footer */
.footer-links a{position:absolute;color:var(--white);text-decoration:none;font-family:"Poppins",sans-serif;font-size:17px;letter-spacing:1.5px;white-space:nowrap}
.social{width:36px;height:36px;border-radius:50%;border:2px solid var(--white)}
</style>
</head>
<body>
<div class="page">

  <!-- top bar -->
  <div class="abs topbar">
    <div class="abs hours">
      <div class="badge"><svg width="22" height="22" viewBox="0 0 22 22"><circle cx="11" cy="11" r="10" fill="var(--blue)"/><path d="M11 5v6l4 2" stroke="#fff" stroke-width="2" fill="none" stroke-linecap="round"/></svg></div>
      <span>OPENING HOURS- MON To FRI 10 AM TO 7 PM</span>
    </div>
    <div class="abs phone">
      <div class="badge"><svg width="22" height="22" viewBox="0 0 24 24"><path fill="var(--blue)" d="M6.6 10.8a15 15 0 0 0 6.6 6.6l2.2-2.2a1 1 0 0 1 1-.25 11.4 11.4 0 0 0 3.6.57 1 1 0 0 1 1 1V20a1 1 0 0 1-1 1A17 17 0 0 1 3 4a1 1 0 0 1 1-1h3.5a1 1 0 0 1 1 1c0 1.25.2 2.45.57 3.57a1 1 0 0 1-.25 1z"/></svg></div>
      <span>555-014-2290</span>
    </div>
  </div>

  <!-- nav -->
  <div class="abs brand"><span class="dot"></span><span>ANDEVIA</span></div>
  <nav class="abs nav" style="left:0;top:116px;width:1200px">
    <a style="left:503px">Home</a>
    <a style="left:606px">About Us</a>
    <a style="left:736px">services</a>
    <a style="left:861px">Product</a>
    <a style="left:982px">Contact Us</a>
  </nav>

  <!-- hero -->
  <svg class="abs hero" width="1200" height="632" viewBox="0 0 1200 632">
    <defs>
      <linearGradient id="heroSky" x1="0" y1="0" x2="0" y2="1">
        <stop offset="0" stop-color="#4d7fb8"/><stop offset=".35" stop-color="#8aa3bd"/><stop offset=".6" stop-color="#8b7260"/><stop offset="1" stop-color="#5d4a3d"/>
      </linearGradient>
    </defs>
    <path role="img" aria-label="Aerial view of Quito with a Gothic basilica under a blue sky" d="M0 0H1200V560C960 600 700 635 500 628 300 622 130 585 0 555Z" fill="url(#heroSky)"/>
    <path d="M0 555C130 585 300 622 500 628 700 635 960 600 1200 560V568C960 612 700 645 500 638 300 632 130 595 0 563Z" fill="var(--yellow)"/>
  </svg>
  <div class="abs hero-title">ANDEVIA</div>
  <div class="abs hero-sub">Lorem ipsum dolor sit amet, consectetur adipiscing elit, sed do<br>eiusmod tempor incididunt ut labore.</div>
  <div class="abs btn" style="left:513px;top:574px;width:175px;height:46px">GET STARTED</div>

  <!-- welcome -->
  <h2 class="abs sec" style="left:0;top:910px;width:1200px;text-align:center">WELCOME TO <span>ANDEVIA</span></h2>
  <p class="abs body-copy" style="left:180px;top:985px;width:840px;text-align:center">Lorem ipsum dolor sit amet, consectetur adipiscing elit, sed do eiusmod tempor incididunt ut labore et dolore magna aliqua. Quis ipsum suspendisse ultrices gravida. Risus commodo viverra maecenas accumsan lacus vel facilisis. sed do eiusmod tempor incididunt ut labore et dolore magna aliqua. Quis ipsum suspendisse ultrices gravida. Risus commodo viverra maecenas.</p>
  <div class="abs btn" style="left:408px;top:1170px;width:177px;height:47px">CONTACT US</div>
  <div class="abs btn" style="left:613px;top:1170px;width:177px;height:47px">READ MORE</div>

  <!-- commodities -->
  <svg class="abs" style="left:0;top:1310px" width="1200" height="820" viewBox="0 0 1200 820">
    <defs>
      <linearGradient id="cream" x1="0" y1="0" x2="1" y2="1">
        <stop offset="0" stop-color="#f7ebdf"/><stop offset=".5" stop-color="#fdf3e8"/><stop offset="1" stop-color="#f3e3d3"/>
      </linearGradient>
    </defs>
    <path role="img" aria-label="Faded port with shipping containers and an airplane, edged by a chocolate splash along the bottom" d="M0 40C120 10 280 10 420 25 640 50 860 70 1200 45V700C1050 760 900 790 700 800 450 810 250 780 0 720Z" fill="url(#cream)"/>
    <path d="M0 40C120 10 280 10 420 25 640 50 860 70 1200 45V50C860 76 640 56 420 31 280 16 120 16 0 46Z" fill="var(--yellow)"/>
    <path d="M0 720C250 780 450 810 700 800 900 790 1050 760 1200 700V714C1050 776 900 806 700 816 450 826 250 796 0 734Z" fill="var(--yellow)"/>
  </svg>
  <h2 class="abs sec" style="left:0;top:1428px;width:1200px;text-align:center">COMMODITIES WE EXPORT</h2>

  <svg class="abs" style="left:126px;top:1522px" width="250" height="250" viewBox="0 0 250 250">
    <path d="M232 118A110 110 0 0 1 55 205 L70 190 A95 95 0 0 0 218 118Z" fill="var(--yellow)"/>
    <circle role="img" aria-label="Bouquet of roses and wildflowers" cx="118" cy="115" r="108" fill="#9a6b63" stroke="#fff" stroke-width="3"/>
  </svg>
  <svg class="abs" style="left:473px;top:1522px" width="250" height="250" viewBox="0 0 250 250">
    <path d="M232 118A110 110 0 0 1 55 205 L70 190 A95 95 0 0 0 218 118Z" fill="var(--yellow)"/>
    <circle role="img" aria-label="Chocolate truffles on a wooden plate" cx="118" cy="115" r="108" fill="#5a3626" stroke="#fff" stroke-width="3"/>
  </svg>
  <svg class="abs" style="left:820px;top:1522px" width="250" height="250" viewBox="0 0 250 250">
    <path d="M232 118A110 110 0 0 1 55 205 L70 190 A95 95 0 0 0 218 118Z" fill="var(--yellow)"/>
    <circle role="img" aria-label="Bunch of ripe bananas" cx="118" cy="115" r="108" fill="#c9951e" stroke="#fff" stroke-width="3"/>
  </svg>

  <div class="abs commodity" style="left:92px;top:1801px"><h3>FLOWERS</h3><p>Lorem ipsum dolor sit amet, consectetur adipiscing elit, sed do eiusmod tempor</p></div>
  <div class="abs commodity" style="left:450px;top:1801px"><h3>CHOCOLATE</h3><p>Neque porro quisquam est qui dolorem ipsum quia dolor sit amet, consectetur.</p></div>
  <div class="abs commodity" style="left:793px;top:1801px"><h3>BANANAS</h3><p>Lorem ipsum dolor sit amet, consectetur adipiscing elit, sed do eiusmod tempor</p></div>

  <!-- benefits -->
  <h2 class="abs sec" style="left:106px;top:2222px">OUR BENEFITS</h2>
  <p class="abs body-copy" style="left:109px;top:2290px;width:450px">Lorem ipsum dolor sit amet, consectetur adipiscing elit, sed do eiusmod tempor incididunt ut labore et dolore magna aliqua.</p>
  <div class="abs benefit" style="top:2418px"><span class="ico"><svg width="30" height="30" viewBox="0 0 30 30" fill="none" stroke="#333" stroke-width="2"><rect x="5" y="10" width="20" height="14"/><path d="M5 16h20M13 10v14"/></svg></span><span>Lorem ipsum dolor sit amet, consectetur adipiscing elit, sed do eiusmod.</span></div>
  <div class="abs benefit" style="top:2519px"><span class="ico"><svg width="30" height="30" viewBox="0 0 30 30" fill="none" stroke="#333" stroke-width="2"><rect x="3" y="9" width="16" height="12"/><path d="M19 13h5l3 4v4h-8"/><circle cx="8" cy="23" r="2"/><circle cx="22" cy="23" r="2"/></svg></span><span>Neque porro quisquam est qui dolorem ipsum quia dolor sit amet.</span></div>
  <div class="abs benefit" style="top:2614px"><span class="ico"><svg width="30" height="30" viewBox="0 0 30 30" fill="none" stroke="#333" stroke-width="2"><path d="M4 24h22M6 16l18-6-2 5-9 3-4 4z"/></svg></span><span>Sed ut perspiciatis unde omnis iste natus error sit voluptatem.</span></div>

  <div class="abs" style="left:629px;top:2252px;width:538px;height:418px;background:var(--blue)"></div>
  <div class="abs" role="img" aria-label="Container truck at a port yard with stacked shipping containers" style="left:642px;top:2250px;width:558px;height:408px;border:4px solid var(--yellow);border-right:none;background:linear-gradient(180deg,#6f9fd0 0%,#b9cde0 45%,#8c8f94 70%,#6c6d70 100%)"></div>

  <!-- why choose us -->
  <svg class="abs" style="left:0;top:2780px" width="1200" height="620" viewBox="0 0 1200 620">
    <path role="img" aria-label="Harbour with container cranes in blue tone" d="M0 45C200 25 400 12 620 12 850 12 1050 18 1200 30V515C1050 545 850 560 620 575 400 590 150 580 0 555Z" fill="var(--blue)"/>
    <path d="M0 45C200 25 400 12 620 12 850 12 1050 18 1200 30V24C1050 10 850 4 620 4 400 4 200 17 0 37Z" fill="var(--yellow)"/>
    <path d="M0 555C150 580 400 590 620 575 850 560 1050 545 1200 515V527C1050 557 850 572 620 587 400 602 150 592 0 567Z" fill="var(--yellow)"/>
    <circle role="img" aria-label="Cargo ship docked at sunset" cx="110" cy="305" r="255" fill="#6a4a44" stroke="#fff" stroke-width="6"/>
  </svg>
  <div class="abs ring" style="left:273px;top:2871px"><svg width="34" height="34" viewBox="0 0 34 34" fill="none" stroke="#fff" stroke-width="2"><rect x="4" y="9" width="26" height="14"/><path d="M9 9v14M14 9v14M19 9v14M24 9v14"/><circle cx="10" cy="27" r="2"/><circle cx="24" cy="27" r="2"/></svg></div>
  <div class="abs ring" style="left:325px;top:2985px"><svg width="34" height="34" viewBox="0 0 34 34" fill="none" stroke="#fff" stroke-width="2"><circle cx="17" cy="17" r="12"/><path d="M5 17h24M17 5c-5 6-5 18 0 24M17 5c5 6 5 18 0 24"/></svg></div>
  <div class="abs ring" style="left:320px;top:3132px"><svg width="34" height="34" viewBox="0 0 34 34" fill="none" stroke="#fff" stroke-width="2"><path d="M4 28h26M6 19l22-8-3 6-11 4-5 5z"/></svg></div>
  <div class="abs ring" style="left:230px;top:3248px"><svg width="34" height="34" viewBox="0 0 34 34" fill="none" stroke="#fff" stroke-width="2"><path d="M8 6v22h20M12 12h10v10H12z"/></svg></div>

  <h2 class="abs sec" style="left:505px;top:2922px;color:var(--white)">WHY CHOOSE US</h2>
  <p class="abs why-copy" style="left:505px;top:2990px;width:570px">Lorem ipsum dolor sit amet, consectetur adipiscing elit, sed do eiusmod tempor incididunt ut labore et dolore magna aliqua. Quis ipsum suspendisse ultrices gravida. Risus commodo viverra maecenas accumsan lacus vel facilisis. abore et dolore magna aliqua. Quis ipsum suspendisse ultrices gravida.</p>
  <div class="abs btn" style="left:506px;top:3204px;width:177px;height:47px">READ MORE</div>

  <!-- newsletter -->
  <div class="abs news-title" style="left:115px;top:3540px">SIGN UP FOR <span>NEWSLETTER</span></div>
  <div class="abs" style="left:115px;top:3592px;font-size:20px;letter-spacing:.5px;color:#333">Be the First to Know. Sign up to newsletter today</div>
  <div class="abs" style="left:654px;top:3550px;width:393px;height:64px;border:2px solid #cfcfcf;display:flex">
    <div style="flex:1;display:flex;align-items:center;padding-left:28px;font-size:16px;color:#444">Enter your Email Address</div>
    <div style="width:150px;background:var(--yellow);display:flex;align-items:center;justify-content:center;gap:10px;font-family:'Poppins',sans-serif;font-size:16px;color:#222"><svg width="18" height="14" viewBox="0 0 18 14"><rect width="18" height="14" rx="1" fill="#222"/><path d="M1 1l8 6 8-6" stroke="var(--yellow)" stroke-width="1.6" fill="none"/></svg>SUBSCRIBE</div>
  </div>

  <!-- footer -->
  <svg class="abs" style="left:0;top:3735px" width="1200" height="327" viewBox="0 0 1200 327">
    <path role="img" aria-label="Dark container port at night" d="M0 110C250 40 450 15 620 15 820 15 1000 45 1200 105V327H0Z" fill="var(--footer)"/>
    <path d="M0 110C250 40 450 15 620 15 820 15 1000 45 1200 105V97C1000 37 820 7 620 7 450 7 250 32 0 102Z" fill="var(--yellow)"/>
    <line x1="110" y1="283" x2="445" y2="283" stroke="#888" stroke-width="1"/>
    <line x1="755" y1="283" x2="1090" y2="283" stroke="#888" stroke-width="1"/>
  </svg>
  <div class="abs footer-links" style="left:0;top:3860px;width:1200px">
    <a style="left:307px">Home</a>
    <a style="left:409px">About Us</a>
    <a style="left:540px">services</a>
    <a style="left:665px">Product</a>
    <a style="left:786px">Contact Us</a>
  </div>
  <div class="abs social" style="left:530px;top:3929px"></div>
  <div class="abs social" style="left:580px;top:3929px"></div>
  <div class="abs social" style="left:629px;top:3929px"></div>
  <div class="abs" style="left:0;top:4007px;width:1200px;text-align:center;color:var(--white);font-family:'Poppins',sans-serif;font-size:16px">Copyrights 2020. All rights reserved</div>

</div>
</body>
</html>
```